Bref créative
Stationary for a Home Builder
Calvin Morrow
Professional
Calvin Morrow, MBA
Owner
4827 Pelham Crescent
Edmonton, AB
T6R 2J8
calvin@rpbbuilds.com
rpbbuilds.com
For the business card you may want to delete the 'rpbbuilds.com' at the bottom which is currently on the AI file provided.
I'd like to have the logo on the back of the card with enough white space to allow hand written notes to be added.
Logo - White and Blue - AI
Logo - White and Blue - EPS
Logo - Black and Blue - AI
Logo - Black and Blue - EPS

```html
<!DOCTYPE html>
<html lang="en">
<head>
<meta charset="utf-8">
<title>RPB Builds — Business Card</title>
<link href="https://fonts.googleapis.com/css2?family=Montserrat:wght@400;500;700&display=swap" rel="stylesheet">
<style>
  :root {
    --stage: #e6e7ea;
    --card: #ffffff;
    --blue: #1f6ec6;
    --blue-deep: #195fae;
    --ink: #1b1b1d;
    --white: #ffffff;
  }
  html, body {
    margin: 0;
    width: 1200px;
    height: 908px;
    overflow: hidden;
    background: var(--stage);
    font-family: "Montserrat", Arial, sans-serif;
  }
  .canvas {
    position: relative;
    width: 1200px;
    height: 908px;
  }
  .card {
    position: absolute;
    top: 104px;
    width: 400px;
    height: 700px;
    background: var(--card);
    border-radius: 28px;
    overflow: hidden;
    box-shadow: 0 2px 10px rgba(0,0,0,0.12);
  }
  .card--back { left: 160px; }
  .card--front { left: 640px; }
  .card__band {
    position: absolute;
    inset: 0;
  }
  .brand {
    position: absolute;
    display: flex;
    align-items: center;
    gap: 12px;
    color: var(--ink);
    font-weight: 700;
    font-size: 40px;
    letter-spacing: -0.5px;
  }
  .brand__mark {
    width: 20px;
    height: 20px;
    background: var(--blue);
  }
  .card--back .brand { left: 44px; top: 400px; }
  .card--front .brand { left: 96px; top: 130px; }
  .back-url {
    position: absolute;
    left: 30px;
    bottom: 34px;
    color: var(--white);
    font-weight: 700;
    font-size: 30px;
  }
  .holder {
    position: absolute;
    left: 40px;
    top: 258px;
    width: 320px;
    color: var(--ink);
  }
  .holder__name {
    font-weight: 700;
    font-size: 22px;
    margin: 0;
  }
  .holder__role {
    font-weight: 500;
    font-size: 16px;
    margin: 4px 0 0;
    text-align: right;
    padding-right: 22px;
  }
  .contact {
    position: absolute;
    left: 44px;
    top: 388px;
    color: var(--white);
    font-size: 18px;
    line-height: 1.42;
  }
  .contact p { margin: 0; }
  .contact__row {
    display: flex;
    align-items: center;
    gap: 10px;
  }
  .contact__icon {
    width: 18px;
    height: 18px;
    flex: none;
  }
</style>
</head>
<body>
<main class="canvas">

  <section class="card card--back" aria-label="Card back">
    <svg class="card__band" viewBox="0 0 400 700" aria-hidden="true">
      <polygon points="0,548 196,548 400,610 400,700 0,700" fill="var(--blue)"/>
      <line x1="196" y1="548" x2="300" y2="548" stroke="var(--blue)" stroke-width="2"/>
      <line x1="300" y1="534" x2="300" y2="562" stroke="var(--blue)" stroke-width="2"/>
    </svg>
    <div class="brand"><span class="brand__mark"></span>RPB Builds</div>
    <div class="back-url">rpbbuilds.com</div>
  </section>

  <section class="card card--front" aria-label="Card front">
    <svg class="card__band" viewBox="0 0 400 700" aria-hidden="true">
      <polygon points="0,340 196,340 400,412 400,700 0,700" fill="var(--blue)"/>
      <line x1="196" y1="340" x2="306" y2="340" stroke="var(--blue)" stroke-width="2"/>
      <line x1="306" y1="326" x2="306" y2="354" stroke="var(--blue)" stroke-width="2"/>
    </svg>
    <div class="brand"><span class="brand__mark"></span>RPB Builds</div>
    <div class="holder">
      <p class="holder__name">Calvin Morrow, MBA</p>
      <p class="holder__role">Owner</p>
    </div>
    <div class="contact">
      <p>4827 Pelham Crescent</p>
      <p>Edmonton, AB</p>
      <p>T6R 2J8</p>
      <p class="contact__row">
        <svg class="contact__icon" viewBox="0 0 18 18" aria-hidden="true"><circle cx="9" cy="9" r="9" fill="var(--white)"/><path d="M6 4.5l1.6 2.4-1 1a6 6 0 0 0 3.5 3.5l1-1L13.5 12l-1 1.5C8.5 13.5 4.5 9.5 4.5 5.5z" fill="var(--blue)"/></svg>
        780.555.0147
      </p>
      <p class="contact__row">
        <svg class="contact__icon" viewBox="0 0 18 18" aria-hidden="true"><circle cx="9" cy="9" r="9" fill="var(--white)"/><rect x="4.5" y="5.5" width="9" height="7" fill="none" stroke="var(--blue)" stroke-width="1.3"/><path d="M4.5 5.5L9 9.5l4.5-4" fill="none" stroke="var(--blue)" stroke-width="1.3"/></svg>
        calvin@rpbbuilds.com
      </p>
      <p class="contact__row">
        <svg class="contact__icon" viewBox="0 0 18 18" aria-hidden="true"><circle cx="9" cy="9" r="9" fill="var(--white)"/><circle cx="9" cy="9" r="4.8" fill="none" stroke="var(--blue)" stroke-width="1.2"/><ellipse cx="9" cy="9" rx="2" ry="4.8" fill="none" stroke="var(--blue)" stroke-width="1.1"/><line x1="4.2" y1="9" x2="13.8" y2="9" stroke="var(--blue)" stroke-width="1.1"/></svg>
        rpbbuilds.com
      </p>
    </div>
  </section>

</main>
</body>
</html>
```